School Management website

I need page design for our school management system website

Base website is www.brindavo.com. When the student logs in, he will reach the below pages.
You can either design with white and blue background or grey and white background

Page 1 - School Info

Header
product name("Brindavo") in left corner
logout link in right corner

LeftMenu

Dashboard
School Info
School Settings
Staffs
Classes
Messaging
Contact Us

Footer
About link and copyright text

School Info content
The page should have breadcrumb

The content of this page will be the school profile
We have to show the school logo
Name
School Type
School Code
School Count
School Address
School phone 1&2
School Email
School Website

The page content should show edit school profile link which will take the user to another page

```html
<!DOCTYPE html>
<html lang="en">
<head>
<meta charset="utf-8">
<title>Brindavo – School Info</title>
<link rel="stylesheet" href="https://fonts.googleapis.com/css2?family=Roboto+Condensed:wght@400;700&family=Open+Sans:wght@700&display=swap">
<style>
:root{
  --page-bg:#f0f0f0;
  --header-top:#ffffff;
  --header-bottom:#e9e9e9;
  --header-line:#c9c9c9;
  --brand-blue:#1f8fcc;
  --menu-blue:#1b76b0;
  --menu-text:#444444;
  --icon:#4a4a4a;
  --crumb-top:#4a4747;
  --crumb-bottom:#2e2c2c;
  --crumb-text:#a9a9a9;
  --panel:#ffffff;
  --row-bg:#f6f6f6;
  --row-line:#d6d6d6;
  --cell-text:#3a3a3a;
  --edit-bg:#676767;
  --footer-bg:#1e1e1e;
  --footer-text:#bdbdbd;
  --footer-link:#2a9ad8;
}
*{box-sizing:border-box;margin:0;padding:0}
html,body{width:1200px;height:839px;overflow:hidden}
body{position:relative;background:var(--page-bg);font-family:"Roboto Condensed",Arial,sans-serif;color:var(--cell-text)}

.site-header{position:absolute;left:0;top:0;width:1200px;height:58px;background:linear-gradient(var(--header-top),var(--header-bottom));border-bottom:1px solid var(--header-line)}
.brand{position:absolute;left:40px;top:11px;font-family:"Open Sans",Arial,sans-serif;font-weight:700;font-size:30px;letter-spacing:-.5px;color:var(--brand-blue)}
.logout{position:absolute;left:1079px;top:17px;width:83px;height:28px;border-radius:14px;background:linear-gradient(#49b3ea,#1d86c7);border:1px solid #1673ad;display:flex;align-items:center;padding-left:4px;color:#fff;font-family:"Open Sans",Arial,sans-serif;font-weight:700;font-size:12px;text-decoration:none}
.logout .lock{width:22px;height:22px;border-radius:50%;background:#fff;display:flex;align-items:center;justify-content:center;margin-right:6px}

.side-menu{position:absolute;left:32px;top:84px;width:202px;list-style:none}
.side-menu li{height:50px;display:flex;align-items:center;padding-left:6px;font-size:15px;text-transform:uppercase;color:var(--menu-text)}
.side-menu li svg{width:28px;height:28px;margin-right:12px;fill:var(--icon)}
.side-menu .dashboard{color:var(--menu-blue);font-size:17px;margin-bottom:25px;height:48px}
.side-menu .active{background:var(--panel);color:var(--menu-blue);border-radius:8px 0 0 8px;height:46px;margin-bottom:4px}

.breadcrumb{position:absolute;left:235px;top:90px;width:917px;height:34px;border-radius:6px;background:linear-gradient(var(--crumb-top),var(--crumb-bottom));display:flex;align-items:center;font-size:13px;color:var(--crumb-text);text-transform:uppercase}
.breadcrumb .crumb{display:flex;align-items:center;height:100%}
.breadcrumb .sep{width:12px;height:34px;margin:0 14px}

.content{position:absolute;left:234px;top:130px;width:919px;height:650px;background:var(--panel);border-radius:0 8px 8px 8px}
.school-logo{position:absolute;left:64px;top:62px;font-family:"Roboto Condensed",Arial,sans-serif;font-weight:700;font-size:26px;color:var(--brand-blue)}
.edit-link{position:absolute;left:827px;top:58px;width:59px;height:29px;border-radius:8px;background:var(--edit-bg);color:#fff;font-family:"Open Sans",Arial,sans-serif;font-weight:700;font-size:15px;display:flex;align-items:center;justify-content:center;text-decoration:none}

.profile{position:absolute;left:25px;top:105px;width:874px;border:1px solid var(--row-line);border-radius:6px;overflow:hidden;border-collapse:separate;border-spacing:0;background:var(--row-bg)}
.profile tr{height:50px}
.profile td{font-size:17px;border-bottom:2px solid var(--row-line);vertical-align:middle}
.profile tr:last-child td{border-bottom:none}
.profile th{font-weight:400;font-size:17px;text-align:left;width:191px;padding-left:42px;border-bottom:2px solid var(--row-line);position:relative}
.profile tr:last-child th{border-bottom:none}
.profile th::after{content:"";position:absolute;right:0;top:8px;bottom:8px;width:1px;background:#c4c4c4}
.profile td{padding-left:33px}

.site-footer{position:absolute;left:0;top:788px;width:1200px;height:51px;background:var(--footer-bg);font-size:12px;color:var(--footer-text)}
.site-footer p{position:absolute;right:60px;top:18px}
.site-footer a{color:var(--footer-link);text-decoration:none}
</style>
</head>
<body>
<header class="site-header">
  <div class="brand">Brindavo</div>
  <a class="logout" href="#">
    <span class="lock"><svg width="12" height="14" viewBox="0 0 12 14"><path d="M3 6V4a3 3 0 0 1 6 0v2" fill="none" stroke="#1d86c7" stroke-width="2"/><rect x="1" y="6" width="10" height="8" rx="1" fill="#1d86c7"/></svg></span>Logout
  </a>
</header>

<ul class="side-menu">
  <li class="dashboard"><svg viewBox="0 0 28 28"><circle cx="14" cy="14" r="11" fill="none" stroke="#4a4a4a" stroke-width="2"/><path d="M14 14 L20 9" stroke="#4a4a4a" stroke-width="2"/><circle cx="14" cy="14" r="2"/></svg>Dashboard</li>
  <li class="active"><svg viewBox="0 0 28 28"><circle cx="14" cy="14" r="11" fill="none" stroke="#4a4a4a" stroke-width="2"/><rect x="12.5" y="12" width="3" height="9"/><circle cx="14" cy="8.5" r="1.8"/></svg>School Info</li>
  <li><svg viewBox="0 0 28 28"><path d="M12 2h4l1 4 3 1.5 3.5-2 3 3-2 3.5L26 15l-4 1-1.5 3 2 3.5-3 3-3.5-2L16 26h-4l-1-4-3-1.5-3.5 2-3-3 2-3.5L2 13V15l4-1 1.5-3-2-3.5 3-3 3.5 2L12 2z"/><circle cx="14" cy="14" r="4" fill="#f0f0f0"/></svg>School Settings</li>
  <li><svg viewBox="0 0 28 28"><circle cx="11" cy="8" r="5"/><path d="M1 25c0-6 4-10 10-10s10 4 10 10z"/><circle cx="20" cy="13" r="3.5"/><path d="M16 25c0-4 2-7 6-7s5 3 5 7z"/></svg>Staffs</li>
  <li><svg viewBox="0 0 28 28"><rect x="10" y="3" width="16" height="15" fill="none" stroke="#4a4a4a" stroke-width="2"/><circle cx="5" cy="6" r="3"/><path d="M2 11h7l5 3v2l-5-1v12H3z"/><path d="M16 22l2-2 2 2" fill="none" stroke="#4a4a4a" stroke-width="1.5"/></svg>Classes</li>
  <li><svg viewBox="0 0 28 28"><ellipse cx="11" cy="11" rx="10" ry="7"/><path d="M4 16l-2 5 6-3z"/><ellipse cx="18" cy="16" rx="9" ry="6" fill="#4a4a4a" stroke="#f0f0f0" stroke-width="1.5"/><path d="M24 20l2 4-5-2z"/></svg>Messaging</li>
  <li><svg viewBox="0 0 28 28"><circle cx="14" cy="14" r="12" fill="none" stroke="#4a4a4a" stroke-width="2"/><path d="M9 7l3 0 1 4-2 1.5c1 2 2.5 3.5 4.5 4.5L17 15l4 1v3c-6 1-13-6-12-12z"/></svg>Contact Us</li>
</ul>

<nav class="breadcrumb">
  <span class="crumb" style="padding-left:14px"><svg width="20" height="16" viewBox="0 0 20 16"><path d="M10 1L1 9h3v6h4v-4h4v4h4V9h3z" fill="#bdbdbd"/></svg></span>
  <svg class="sep" viewBox="0 0 12 34"><path d="M1 0l10 17L1 34" fill="none" stroke="#777" stroke-width="1.5"/></svg>
  <span class="crumb">Dashboard</span>
  <svg class="sep" viewBox="0 0 12 34"><path d="M1 0l10 17L1 34" fill="none" stroke="#777" stroke-width="1.5"/></svg>
  <span class="crumb">School Info</span>
  <svg class="sep" viewBox="0 0 12 34"><path d="M1 0l10 17L1 34" fill="none" stroke="#777" stroke-width="1.5"/></svg>
</nav>

<main class="content">
  <div class="school-logo">Brindavo</div>
  <a class="edit-link" href="#">Edit</a>
  <table class="profile">
    <tr><th>Name</th><td>ABC</td></tr>
    <tr><th>School Type</th><td>ABC</td></tr>
    <tr><th>School Code</th><td>1023654</td></tr>
    <tr><th>School Count</th><td>65897</td></tr>
    <tr><th>School Address</th><td>ABC, State, City, Country.</td></tr>
    <tr><th>School Phone 1&amp;2</th><td>091-4721-3096-27</td></tr>
    <tr><th>School Email</th><td>office@brindavo.com</td></tr>
    <tr><th>School Website</th><td>www.brindavo.com</td></tr>
  </table>
</main>

<footer class="site-footer">
  <p><a href="#">About Us</a> / Copyright © 2014 &nbsp;|&nbsp; All Rights Reserved</p>
</footer>
</body>
</html>
```